Dunmore Heating and Cooling Stationary Package

We need Stationary package including invoice layout ( drawing attached )
Use our Company LOGO (attached)
Word Doc with requirements /Specs ( attached )
Dunmore Heating & Cooling
(204) 538-1162
214 - 330 Wexcombe Road
Winnipeg, MB R3K 5P8

Business Cards 2 sided printing with Rounded Corners

Notes for Business Cards

Front Side to include the tag Line “Affordable Comfort”
Residential, Custom Build, Builder

Back Side to include Services

• Heating
• Air Conditioning
• Indoor Air Quality
• Gas Fitting
• Ventilation
• Hot Water Tanks
• Service - Repair

Tomas Delacruzo
Owner
tomas@dunmoreheatco.example

Ruel Delacruzo
Co - Owner
ruel@dunmoreheatco.example

Dante Delacruzo
Technician
dante.delacruzo@dunmoreheatco.example

Greg Volkov
Residential Sales Manager
greg.volkov@dunmoreheatco.example

Linda Volkov
Sales Consultant
linda.volkov@dunmoreheatco.example

Letterhead,

to include the tag Line “Affordable Comfort”

Presentation Folder

Open
48.3 x 30.5 cm
Closed
241 x 305 mm
Finished artwork should use the full bleed dimensions for best results.
Link to Qualo Press Below

http://www.qualopress.example/presentation-folders.aspx?txi=29481&xnid=TopNav_Presentation+Folders+(Clone)+(linked+item)_Marketing+Materials&xnav=TopNav

Envelope #10

10X13 Envelope for Presentation Folder

Lables for Manufactures Brochures

1X4 Label with logo with Address

2X4 Label with Logo and Address

Smaller Logo image for bottom of email signature

Include “Affordable Comfort”

Invoice

Dunmore Heating & Cooling Header Area SEE SCANED IMAGE
(204) 538-1162
214 - 330 Wexcombe Road
Winnipeg, MB R3K 5P8
info@dunmoreheatco.example

Target Market(s)

Residential

Requirements
Must have
• Try to work within logo colors
Nice to have
• Clean Design

```html
<!DOCTYPE html>
<html lang="en">
<head>
<meta charset="utf-8">
<title>Dunmore Heating &amp; Cooling – 10x13 Envelope</title>
<link href="https://fonts.googleapis.com/css2?family=Open+Sans:wght@400;600;700&display=swap" rel="stylesheet">
<style>
  :root{
    --backdrop:#3a1c16;
    --brand-blue:#3a66ad;
    --brand-blue-dark:#2f5597;
    --brand-orange:#f07f22;
    --brand-yellow:#fbb61a;
    --paper:#ffffff;
    --ink:#222222;
    --title:#ffffff;
  }
  *{margin:0;padding:0;box-sizing:border-box}
  html,body{width:1200px;height:862px;overflow:hidden}
  body{background:var(--backdrop);font-family:"Open Sans",Arial,sans-serif;position:relative}
  .sheet-title{
    position:absolute;top:34px;left:0;width:1200px;text-align:center;
    color:var(--title);font-size:20px;font-weight:400;letter-spacing:1px;
  }
  .envelope{position:absolute;width:496px;height:740px;background:var(--paper);overflow:hidden}
  .envelope--first{left:77px;top:80px}
  .envelope--second{left:632px;top:88px;height:735px}
  .envelope__flap{position:absolute;left:0;top:0;width:496px;height:90px;display:block}
  .envelope__flap-line{
    position:absolute;top:19px;left:0;width:100%;text-align:center;
    transform:rotate(180deg);color:#fff;font-size:8.5px;font-style:italic;
  }
  .envelope__flap-mark{
    position:absolute;top:44px;left:241px;width:14px;height:14px;background:var(--brand-orange);
  }
  .brand{position:absolute;left:44px;top:150px}
  .brand__name{
    display:flex;align-items:center;gap:8px;
    font-weight:700;font-size:15px;color:var(--ink);line-height:1;
  }
  .brand__square{width:22px;height:22px;background:var(--brand-orange)}
  .brand__tagline{
    margin:4px 0 0 30px;font-size:9px;font-weight:700;color:var(--brand-orange);
  }
  .return-address{
    position:absolute;left:44px;top:214px;font-size:8.5px;line-height:1.3;color:var(--ink);font-style:normal;
  }
  .envelope__footer-band{
    position:absolute;left:0;bottom:0;width:100%;height:100px;
    background:linear-gradient(180deg,var(--brand-yellow) 0%,var(--brand-orange) 28%,var(--brand-blue) 45%,var(--brand-blue-dark) 100%);
  }
</style>
</head>
<body>
  <h1 class="sheet-title">10X13 ENVELOP</h1>

  <section class="envelope envelope--first">
    <svg class="envelope__flap" viewBox="0 0 496 90" aria-hidden="true">
      <defs>
        <linearGradient id="flapFill" x1="0" y1="0" x2="0" y2="1">
          <stop offset="0" stop-color="#4470b6"/><stop offset="1" stop-color="#2f5597"/>
        </linearGradient>
      </defs>
      <path d="M0 90 L12 32 Q16 13 40 10 Q248 -4 456 10 Q480 13 484 32 L496 90 Z" fill="url(#flapFill)"/>
    </svg>
    <p class="envelope__flap-line">“Residential, Custom Build, Builder”</p>
    <span class="envelope__flap-mark"></span>

    <div class="brand">
      <div class="brand__name"><span class="brand__square"></span>Dunmore Heating &amp; Cooling</div>
      <div class="brand__tagline">“Affordable Comfort”</div>
    </div>
    <address class="return-address">
      214 - 330 Wexcombe Road<br>Winnipeg, MB R3K 5P8
    </address>

    <div class="envelope__footer-band" role="img" aria-label="Decorative footer band in brand yellow, orange and blue"></div>
  </section>

  <section class="envelope envelope--second">
    <svg class="envelope__flap" viewBox="0 0 496 90" aria-hidden="true">
      <path d="M0 90 L12 32 Q16 13 40 10 Q248 -4 456 10 Q480 13 484 32 L496 90 Z" fill="url(#flapFill)"/>
    </svg>
    <p class="envelope__flap-line">“Residential, Custom Build, Builder”</p>
    <span class="envelope__flap-mark"></span>

    <div class="brand">
      <div class="brand__name"><span class="brand__square"></span>Dunmore Heating &amp; Cooling</div>
      <div class="brand__tagline">“Affordable Comfort”</div>
    </div>
    <address class="return-address">
      4718 Larchmont Avenue<br>Winnipeg, Manitoba R3J 6T4
    </address>

    <div class="envelope__footer-band" role="img" aria-label="Decorative footer band in brand yellow, orange and blue"></div>
  </section>
</body>
</html>
```